Brivolan - presentation for a remote DBA team offering data platform management

We need a website design for wordpress site called Brivolan.cz
We deliver remote database and data platform administration and development, oversee the database administrators, consult and train the personnel responsible for the database operations. The website should include several sections, home page with graphics elements supporting the name and service - remote dba work; blog section; service introduction and description, team introduction and description, download section for documents, presentations etc.

Target Market(s)

small and medium business companies requiring remote DBA service

Number of Pages Required

3 page

Font styles to use
Sans Serif

Colors

Designer to choose colors to be used in the design.

Requirements
Must have
• The website should have several sections to introduce the services, blog, team introduction, downloads

```html
<!DOCTYPE html>
<html lang="en">
<head>
<meta charset="utf-8">
<title>Brivolan.cz – Remote DBA</title>
<link href="https://fonts.googleapis.com/css2?family=Lato:ital,wght@0,400;0,700;1,400;1,700&family=Montserrat:wght@600;700&family=Raleway:wght@500;600;700&family=Tinos:wght@700&display=swap" rel="stylesheet">
<style>
:root{
  --blue:#1a47c9;
  --blue-light:#1f72dc;
  --blue-text:#0f3fbf;
  --orange:#f7941d;
  --dark:#2b2b2b;
  --white:#ffffff;
  --grey-text:#555a66;
}
*{margin:0;padding:0;box-sizing:border-box}
html,body{width:1200px;height:3965px;overflow:hidden}
body{font-family:'Lato',sans-serif;color:var(--grey-text);background:var(--white);position:relative}
.abs{position:absolute}
.btn{position:absolute;display:flex;align-items:center;justify-content:center;gap:10px;border-radius:30px;font:700 16px 'Lato',sans-serif;color:var(--white);letter-spacing:.3px}
.btn-orange{background:var(--orange);box-shadow:0 4px 8px rgba(0,0,0,.2)}
.btn-outline{border:2px solid var(--white)}
.section-title{position:absolute;left:0;width:1200px;display:flex;justify-content:center;align-items:center;gap:22px;font:600 36px 'Raleway',sans-serif}
.section-title::before,.section-title::after{content:"";width:80px;height:1px;background:currentColor;opacity:.6}
.section-title b{font-weight:700}

/* header */
.site-header{position:absolute;top:0;left:0;width:1200px;height:106px;background:rgba(34,34,34,.95);z-index:3}
.logo{position:absolute;left:79px;top:28px;font:700 38px 'Montserrat',sans-serif;color:var(--orange)}
.nav{position:absolute;left:460px;top:40px;display:flex;gap:44px;font:400 17px 'Lato',sans-serif;color:var(--white)}
.nav .active{position:relative}
.nav .active::after{content:"";position:absolute;left:0;right:0;top:60px;height:3px;background:var(--orange)}
.header-phone{position:absolute;left:965px;top:38px;display:flex;align-items:center;gap:12px;font:700 19px 'Lato',sans-serif;color:var(--white)}
.search-icon{position:absolute;left:908px;top:40px}

/* hero */
.hero{position:absolute;top:0;left:0;width:1200px;height:700px;background:linear-gradient(180deg,#d9dbdd 0%,#eef0f1 55%,#f6f7f7 100%)}
.hero-title{position:absolute;top:245px;width:1200px;text-align:center;font:700 52px 'Tinos',serif;color:#111;letter-spacing:2px}
.hero-text{position:absolute;top:322px;left:300px;width:600px;text-align:center;font:italic 700 15px/27px 'Lato',sans-serif;color:#222}
.arrow-box{position:absolute;top:342px;width:50px;height:50px;display:flex;align-items:center;justify-content:center}

/* services */
.services{position:absolute;top:614px;left:0;width:1200px;height:501px}
.service{position:absolute;top:150px;width:300px;text-align:center;color:var(--white)}
.service h3{margin-top:140px;font:600 21px 'Raleway',sans-serif}
.service p{margin:20px auto 0;width:250px;font:400 13.5px/24px 'Lato',sans-serif}
.service-icon{position:absolute;left:88px;top:0}

/* about */
.about{position:absolute;top:1115px;left:0;width:1200px;height:481px;background:var(--white)}
.about-photo{position:absolute;left:0;top:0;width:600px;height:481px;background:linear-gradient(135deg,#3c4f6e 0%,#8fb4d9 55%,#d4e3f2 100%)}
.about h2{position:absolute;left:659px;top:50px;font:600 36px 'Raleway',sans-serif;color:var(--blue-text)}
.about h2 b{font-family:'Montserrat',sans-serif;font-weight:700}
.about p{position:absolute;left:660px;top:108px;width:460px;font:400 14px/23px 'Lato',sans-serif}

/* presentation */
.presentation{position:absolute;top:1596px;left:0;width:1200px;height:294px}
.presentation h2{position:absolute;top:62px;width:1200px;text-align:center;font:700 35px 'Tinos',serif;color:var(--white)}
.presentation p{position:absolute;top:118px;left:270px;width:660px;text-align:center;font:italic 400 17px/30px 'Lato',sans-serif;color:var(--white)}

/* team */
.team-title{top:1996px;color:var(--blue-text)}
.member{position:absolute;top:2075px;width:238px;height:261px}
.member-photo{width:238px;height:180px;background:linear-gradient(160deg,#c9ced6,#7e8896)}
.member-label{height:81px;background:var(--blue-light);text-align:center;color:var(--white);padding-top:14px}
.member-label h4{font:600 19px 'Raleway',sans-serif}
.member-label span{display:block;margin-top:6px;font:400 14px 'Lato',sans-serif}
.member-featured{background:var(--orange);text-align:center;color:var(--white);padding:22px 22px 0}
.member-featured h4{font:600 19px 'Raleway',sans-serif}
.member-featured .role{font:400 14px 'Lato',sans-serif;margin-top:4px}
.member-featured p{margin-top:20px;font:700 14px/23px 'Lato',sans-serif}
.circles{display:flex;justify-content:center;gap:14px;margin-top:18px}
.circles i{width:38px;height:38px;border:2px solid var(--white);border-radius:50%}

/* contact */
.contact{position:absolute;top:2410px;left:0;width:1200px;height:518px;background:linear-gradient(135deg,#3a3a3a 0%,#4d4d4d 50%,#2e2e2e 100%)}
.contact-title{top:74px;color:var(--orange)}
.field{position:absolute;background:var(--white);font:400 13px 'Lato',sans-serif;color:#666;padding:16px 12px}

/* blog */
.blog-title{top:2990px;color:var(--blue-text)}
.post-photo{position:absolute;background:linear-gradient(135deg,#2c3a55,#6c8fb8)}
.date-badge{position:absolute;width:54px;height:56px;background:var(--blue-light);border:2px solid var(--white);color:var(--white);text-align:center;padding-top:6px;font:700 17px 'Lato',sans-serif}
.date-badge small{display:block;font:400 12px 'Lato',sans-serif}
.post-panel{position:absolute;width:254px;height:230px;background:var(--blue-light);color:var(--white);padding:18px 14px}
.post-panel h4{font:700 16px/22px 'Lato',sans-serif}
.meta{display:flex;gap:18px;margin-top:12px;font:italic 400 12px 'Lato',sans-serif}
.post-panel p{margin-top:10px;font:400 13px/21px 'Lato',sans-serif}
.post-panel a{display:block;margin-top:12px;font:700 14px 'Lato',sans-serif;text-decoration:underline;color:var(--white)}
.post-wide h4{position:absolute;left:613px;top:3365px;width:510px;font:700 17px/25px 'Lato',sans-serif;color:var(--blue-text)}
.post-wide .meta{position:absolute;left:613px;top:3432px;color:#888}
.post-wide p{position:absolute;left:613px;top:3462px;width:510px;font:italic 400 13px/22px 'Lato',sans-serif}
.post-wide a{position:absolute;left:613px;top:3537px;font:700 14px 'Lato',sans-serif;color:var(--orange);text-decoration:underline}

/* footer */
.footer{position:absolute;top:3626px;left:0;width:1200px;height:254px;background:linear-gradient(180deg,var(--blue-light),var(--blue));color:var(--white)}
.footer-col{position:absolute;top:56px;width:250px}
.footer-col h5{font:700 22px 'Raleway',sans-serif}
.footer-col p{margin-top:26px;font:400 13px/22px 'Lato',sans-serif}
.footer-col a{font:700 13px 'Lato',sans-serif;color:var(--white);text-decoration:underline}
.contact-line{display:flex;gap:14px;align-items:flex-start;margin-top:22px;font:400 13px/22px 'Lato',sans-serif}
.social{display:flex;gap:12px;margin-top:26px}
.social i{width:44px;height:44px;border:2px solid var(--white);border-radius:50%}
.copyright{position:absolute;top:3880px;left:0;width:1200px;height:85px;background:var(--orange);display:flex;align-items:center;justify-content:center;font:400 13px 'Lato',sans-serif;color:var(--white)}
</style>
</head>
<body>

<section class="hero" role="img" aria-label="Bright office photo with a laptop on a desk">
  <h1 class="hero-title">BRIVOLAN . CZ</h1>
  <p class="hero-text">Lorem Ipsum is simply dummy text of the printing and typesetting industry. Lorem Ipsum has been the industry's standard dummy text ever since the 1500s.</p>
  <div class="btn btn-orange" style="left:520px;top:403px;width:160px;height:56px">READ MORE</div>
  <div class="arrow-box" style="left:52px;background:var(--white)">
    <svg width="22" height="14" viewBox="0 0 22 14"><path d="M21 7H2M8 1 2 7l6 6" fill="none" stroke="#333" stroke-width="2"/></svg>
  </div>
  <div class="arrow-box" style="left:1098px;background:var(--orange)">
    <svg width="22" height="14" viewBox="0 0 22 14"><path d="M1 7h19M14 1l6 6-6 6" fill="none" stroke="#fff" stroke-width="2"/></svg>
  </div>
</section>

<header class="site-header">
  <div class="logo">Brivolan.cz</div>
  <nav class="nav"><span class="active">Home</span><span>About</span><span>Services</span><span>Blog</span><span>Contact</span></nav>
  <svg class="search-icon" width="22" height="22" viewBox="0 0 22 22"><circle cx="9" cy="9" r="7" fill="none" stroke="#fff" stroke-width="2"/><path d="M14 14l7 7" stroke="#fff" stroke-width="2.5"/></svg>
  <div class="header-phone">
    <svg width="20" height="20" viewBox="0 0 24 24"><path fill="#fff" d="M6.6 10.8a15.1 15.1 0 0 0 6.6 6.6l2.2-2.2a1 1 0 0 1 1-.25 11.4 11.4 0 0 0 3.6.57 1 1 0 0 1 1 1V20a1 1 0 0 1-1 1A17 17 0 0 1 3 4a1 1 0 0 1 1-1h3.5a1 1 0 0 1 1 1c0 1.25.2 2.450.57 3.57a1 1 0 0 1-.25 1z"/></svg>
    555-014-2270
  </div>
</header>

<section class="services">
  <svg class="abs" style="top:0;left:0" width="1200" height="501" viewBox="0 0 1200 501">
    <defs><linearGradient id="svcGrad" x1="0" y1="0" x2="0" y2="1"><stop offset="0" stop-color="#1a3fc2"/><stop offset="1" stop-color="#1e72dc"/></linearGradient></defs>
    <polygon points="0,60 620,0 1200,55 1200,501 0,501" fill="url(#svcGrad)"/>
  </svg>
  <h2 class="section-title" style="top:76px;color:var(--white)"><span>Our Services</span></h2>

  <div class="service" style="left:88px">
    <svg class="service-icon" width="124" height="124" viewBox="0 0 124 124"><circle cx="62" cy="62" r="60" fill="none" stroke="#fff" stroke-width="2" stroke-dasharray="5 5"/><circle cx="62" cy="62" r="48" fill="#f7941d"/><rect x="44" y="40" width="22" height="40" rx="2" fill="none" stroke="#fff" stroke-width="2.5"/><rect x="62" y="55" width="20" height="28" rx="2" fill="none" stroke="#fff" stroke-width="2.5"/><path d="M49 48h12M49 56h12M49 64h8" stroke="#fff" stroke-width="2.5"/></svg>
    <h3>Remote database</h3>
    <p>Lorem Ipsum is simply dummy text of the printing and typesetting industry. Lorem Ipsum ever since the 1500s.</p>
  </div>
  <div class="service" style="left:450px">
    <svg class="service-icon" width="124" height="124" viewBox="0 0 124 124"><circle cx="62" cy="62" r="60" fill="none" stroke="#fff" stroke-width="2" stroke-dasharray="5 5"/><circle cx="62" cy="62" r="48" fill="#f7941d"/><rect x="40" y="42" width="18" height="14" fill="none" stroke="#fff" stroke-width="2.5"/><rect x="40" y="66" width="18" height="14" fill="none" stroke="#fff" stroke-width="2.5"/><rect x="68" y="54" width="18" height="14" fill="none" stroke="#fff" stroke-width="2.5"/><path d="M58 49h5v24h-5M63 61h5" fill="none" stroke="#fff" stroke-width="2.5"/></svg>
    <h3>Data platform administration</h3>
    <p>Lorem Ipsum is simply dummy text of the printing and typesetting industry. Lorem Ipsum ever since the 1500s.</p>
  </div>
  <div class="service" style="left:815px">
    <svg class="service-icon" width="124" height="124" viewBox="0 0 124 124"><circle cx="62" cy="62" r="60" fill="none" stroke="#fff" stroke-width="2" stroke-dasharray="5 5"/><circle cx="62" cy="62" r="48" fill="#f7941d"/><rect x="46" y="36" width="30" height="52" rx="4" fill="none" stroke="#fff" stroke-width="2.5"/><circle cx="66" cy="66" r="9" fill="none" stroke="#fff" stroke-width="2.5"/><path d="M56 44h10" stroke="#fff" stroke-width="2.5"/></svg>
    <h3>Development</h3>
    <p>Lorem Ipsum is simply dummy text of the printing and typesetting industry. Lorem Ipsum ever since the 1500s.</p>
  </div>
</section>

<section class="about">
  <div class="about-photo" role="img" aria-label="Businessman holding devices connected to a glowing globe network"></div>
  <h2>About <b>BRIVOLAN.cz</b></h2>
  <p>Lorem Ipsum is simply dummy text of the printing and typesetting industry. Lorem Ipsum has been the industry's standard dummy text ever since the 1500s, when an unknown printer took a galley of type and scrambled it to make a type specimen book. It has survived not five centuries, but also the leap into electronic typesetting, remaining essentially unchanged. It was popularised in the 1960s with the release Quillmark sheets containing Lorem Ipsum passages, and more recently with desktop publishing software like Folioset Layout including versions of Lorem Ipsum.</p>
  <div class="btn btn-orange" style="left:657px;top:369px;width:160px;height:56px">READ MORE</div>
</section>

<section class="presentation">
  <svg class="abs" style="top:0;left:0" width="1200" height="294" viewBox="0 0 1200 294">
    <defs><linearGradient id="presGrad" x1="0" y1="0" x2="1" y2="1"><stop offset="0" stop-color="#1e6fdc"/><stop offset="1" stop-color="#1a3fc2"/></linearGradient></defs>
    <polygon points="0,0 1200,0 1200,242 600,294 0,242" fill="url(#presGrad)"/>
  </svg>
  <h2>Brivolan. cz Presentation</h2>
  <p>Lorem Ipsum is simply dummy text of the printing and typesetting industry. Lorem Ipsum has been the industry's standard dummy text ever since the 1500s.</p>
  <div class="btn btn-outline" style="left:495px;top:207px;width:210px;height:56px">READ MORE
    <svg width="24" height="18" viewBox="0 0 24 18"><path d="M2 8v9h20V8M2 8l10 6 10-6M6 5V1h12v4" fill="none" stroke="#fff" stroke-width="1.6"/></svg>
  </div>
</section>

<h2 class="section-title team-title"><span>Our Technical <b>Team</b></span></h2>

<article class="member" style="left:79px">
  <div class="member-photo" role="img" aria-label="Portrait photo of team member"></div>
  <div class="member-label"><h4>Marek Halden</h4><span>Database Management</span></div>
</article>
<article class="member" style="left:346px">
  <div class="member-photo" role="img" aria-label="Portrait photo of team member"></div>
  <div class="member-label"><h4>Tomas Verin</h4><span>Project Manager</span></div>
</article>
<article class="member member-featured" style="left:616px">
  <h4>Lukas Brenner</h4>
  <div class="role">Quality Planning</div>
  <p>Lukas has had many roles over the years including quality manager at Kovrana.</p>
  <div class="circles"><i></i><i></i></div>
</article>
<article class="member" style="left:883px">
  <div class="member-photo" role="img" aria-label="Portrait photo of team member"></div>
  <div class="member-label"><h4>Pavel Oster</h4><span>Copper Management</span></div>
</article>

<section class="contact" role="img" aria-label="Dark background photo of hands typing on a laptop">
  <h2 class="section-title contact-title"><span>Contact Us</span></h2>
  <div class="field" style="left:140px;top:135px;width:293px;height:63px">Name :</div>
  <div class="field" style="left:452px;top:135px;width:293px;height:63px">Phone :</div>
  <div class="field" style="left:764px;top:135px;width:293px;height:63px">Email :</div>
  <div class="field" style="left:140px;top:220px;width:917px;height:153px">Message :</div>
  <div class="btn btn-outline" style="left:497px;top:397px;width:206px;height:62px;border-radius:0;font-weight:400;font-size:17px">SEND MESSAGE</div>
</section>

<h2 class="section-title blog-title"><span>Recent <b>Blog</b></span></h2>

<div class="post-photo" style="left:79px;top:3074px;width:254px;height:230px" role="img" aria-label="Photo of a smiling man with a headset in an office"></div>
<div class="date-badge" style="left:91px;top:3236px">04<small>Sep</small></div>
<div class="post-panel" style="left:333px;top:3074px">
  <h4>Lorem Ipsum simply dummy printing typesetting industry.</h4>
  <div class="meta"><span>By admin</span><span>12 Comments</span></div>
  <p>Lorem Ipsum is simply dummy text ever since the 1500s.</p>
  <a>READ MORE</a>
</div>

<div class="post-photo" style="left:79px;top:3330px;width:254px;height:230px" role="img" aria-label="Photo of a man working at a computer in a dark room"></div>
<div class="date-badge" style="left:91px;top:3492px">04<small>Sep</small></div>
<div class="post-panel" style="left:333px;top:3330px">
  <h4>Lorem Ipsum simply dummy printing typesetting industry.</h4>
  <div class="meta"><span>By admin</span><span>12 Comments</span></div>
  <p>Lorem Ipsum is simply dummy text ever since the 1500s.</p>
  <a>READ MORE</a>
</div>

<div class="post-wide">
  <div class="post-photo" style="left:613px;top:3074px;width:510px;height:261px" role="img" aria-label="Photo of hands using a phone and a laptop"></div>
  <div class="date-badge" style="left:633px;top:3262px">04<small>Sep</small></div>
  <h4>Lorem Ipsum is simply dummy text of the printing typesetting industry. Lorem Ipsum has industry's standard dummy 1500s.</h4>
  <div class="meta"><span>By admin</span><span>12 Comments</span></div>
  <p>Lorem Ipsum is simply dummy text of the printing and typesetting industry. Lorem Ipsum has been the industry's standard dummy text ever.</p>
  <a>READ MORE</a>
</div>

<footer class="footer">
  <div class="footer-col" style="left:79px">
    <h5>About Us</h5>
    <p>Lorem Ipsum is simply dummy the text of the printing and Printing of typesetting industry. Lorem Ipsum</p>
    <a>READ MORE</a>
  </div>
  <div class="footer-col" style="left:344px">
    <h5>Office Address</h5>
    <div class="contact-line"><svg width="14" height="20" viewBox="0 0 14 20"><path d="M7 0a7 7 0 0 0-7 7c0 5 7 13 7 13s7-8 7-13a7 7 0 0 0-7-7zm0 10a3 3 0 1 1 0-6 3 3 0 0 1 0 6z" fill="#fff"/></svg><span>123, Address, State Name<br>City, Street, Zipcode</span></div>
  </div>
  <div class="footer-col" style="left:608px">
    <h5>Call Us</h5>
    <div class="contact-line"><svg width="16" height="16" viewBox="0 0 24 24"><path fill="#fff" d="M6.6 10.8a15.1 15.1 0 0 0 6.6 6.6l2.2-2.2a1 1 0 0 1 1-.25 11.4 11.4 0 0 0 3.6.57 1 1 0 0 1 1 1V20a1 1 0 0 1-1 1A17 17 0 0 1 3 4a1 1 0 0 1 1-1h3.5a1 1 0 0 1 1 1c0 1.25.2 2.45.57 3.57a1 1 0 0 1-.25 1z"/></svg><span>555-014-2270</span></div>
    <div class="contact-line" style="margin-top:14px"><svg width="16" height="12" viewBox="0 0 16 12"><rect x="1" y="1" width="14" height="10" fill="none" stroke="#fff" stroke-width="1.6"/><path d="M1 1l7 6 7-6" fill="none" stroke="#fff" stroke-width="1.6"/></svg><span>info@brivolan.cz</span></div>
  </div>
  <div class="footer-col" style="left:873px">
    <h5>Follow On</h5>
    <div class="social"><i></i><i></i><i></i><i></i></div>
  </div>
</footer>
<div class="copyright">Copyright ©&nbsp;<b>BRIVOLAN.cz</b>&nbsp;- 2018 . All Right Reserved</div>

</body>
</html>
```